Corvane Project Services - Flyer

Project Breif:
I need a single page A4 Capability Statement, which will be used to market our services to prospective clients, both in print and via email PDF.
It needs to look professional and should incorporate the elements I have uploaded into files, these include:
Capability Statement Text
Corvane Services Company Logo
Additional Logo’s (Tools We Use)
Glimmer Bay Pics can be cut into the page
I have included examples of capability statements as a guide to what i am looking for.
Regards
Derek
Engineering Consulting

```html
<!DOCTYPE html>
<html lang="en">
<head>
<meta charset="utf-8">
<title>Corvane Project Services – Capability Statement</title>
<link href="https://fonts.googleapis.com/css2?family=Cabin:wght@400;500;600&family=Didact+Gothic&display=swap" rel="stylesheet">
<style>
  :root{
    --backdrop:#7d9796;
    --paper:#efefef;
    --blue:#2a5db0;
    --blue-dark:#1f4a91;
    --navy:#1c2a4a;
    --ink:#1d1d1d;
    --line:#3b4a66;
    --white:#ffffff;
  }
  *{margin:0;padding:0;box-sizing:border-box}
  html,body{width:1200px;height:1200px;overflow:hidden;background:var(--backdrop)}
  .flyer{position:absolute;left:197px;top:30px;width:805px;height:1140px;background:var(--paper);overflow:hidden;font-family:"Didact Gothic",sans-serif;color:var(--ink)}
  .abs{position:absolute}

  .brand{left:28px;top:40px;width:180px;text-align:center}
  .brand-dot{width:54px;height:54px;border-radius:50%;background:var(--blue);margin:0 auto 10px}
  .brand-name{font-family:"Cabin",sans-serif;font-weight:600;font-size:15px;letter-spacing:1.5px;color:var(--navy);line-height:1.15}

  .phone{right:27px;top:36px;display:flex;align-items:center;gap:10px;font-family:"Cabin",sans-serif;font-size:23px;font-weight:500;color:var(--ink)}

  .banner{left:0;top:80px;width:805px;height:101px}
  .banner-title{right:22px;top:95px;font-family:"Cabin",sans-serif;font-size:30px;color:var(--white);letter-spacing:.3px}
  .banner-rule{left:296px;top:134px;width:487px;height:2px;background:var(--white)}
  .banner-sub{right:22px;top:142px;font-family:"Cabin",sans-serif;font-size:17.5px;color:var(--white)}

  .hero{left:0;top:181px;width:805px;height:343px;background:linear-gradient(135deg,#7fa3c9 0%,#c9d3dd 45%,#e4e2de 70%,#a8b8cc 100%)}

  .pill{height:32px;background:var(--blue);color:var(--white);font-family:"Cabin",sans-serif;font-weight:500;font-size:21px;line-height:32px;border-radius:0 16px 16px 0;padding-left:24px;box-shadow:2px 2px 0 var(--blue-dark)}
  .pill.services{border-radius:16px;padding-left:22px}

  .copy{left:21px;width:375px;font-size:12px;line-height:14.3px;text-align:justify}
  .copy p{margin:0}

  .timeline{left:433px;top:622px;width:2px;height:340px;background:var(--line)}
  .svc-icon{width:40px;height:40px;border-radius:50%;background:var(--paper);border:3px solid var(--blue);display:flex;align-items:center;justify-content:center}
  .svc-icon span{width:24px;height:24px;border-radius:50%;background:var(--blue);display:flex;align-items:center;justify-content:center}
  .svc-title{font-family:"Cabin",sans-serif;font-size:21px;font-weight:500;color:var(--ink)}
  .svc-title b{font-weight:500;color:var(--blue)}
  .svc-list{list-style:none;font-size:12px;line-height:16px}
  .svc-list.small{font-family:"Cabin",sans-serif;font-size:11.5px}
  .svc-list li{padding-left:12px;position:relative}
  .svc-list li::before{content:"";position:absolute;left:0;top:6px;width:6px;height:6px;border-radius:50%;background:var(--blue-dark)}

  .portrait{left:683px;top:957px;width:90px;height:109px;background:linear-gradient(180deg,#d9d9d9,#a9adb4);border:2px solid #fff}

  .tools{left:22px;top:1085px;display:flex;gap:16px;align-items:center;font-family:"Cabin",sans-serif;font-size:12px;font-weight:600;color:var(--blue-dark)}
  .tools .sq{display:inline-block;width:9px;height:9px;background:var(--blue-dark);margin-right:4px;vertical-align:middle}

  .footer{left:0;top:1044px;width:805px;height:96px}
  .contact{top:1103px;display:flex;align-items:center;gap:10px;font-size:16px;color:var(--white)}
  .divider{left:290px;top:1102px;width:3px;height:24px;background:var(--white)}
  .md-name{right:27px;top:1089px;font-family:"Cabin",sans-serif;font-size:19px;font-weight:500;color:var(--white)}
  .md-role{right:27px;top:1111px;font-family:"Didact Gothic",sans-serif;font-size:16px;color:var(--white)}
</style>
</head>
<body>
<div class="flyer">

  <div class="abs brand">
    <div class="brand-dot"></div>
    <div class="brand-name">CORVANE PROJECT<br>SERVICES</div>
  </div>

  <div class="abs phone">
    <svg width="24" height="24" viewBox="0 0 24 24"><path d="M6.6 10.8a15.1 15.1 0 0 0 6.6 6.6l2.2-2.2c.3-.3.7-.4 1-.2 1.1.4 2.3.6 3.6.6.6 0 1 .4 1 1V20c0 .6-.4 1-1 1A17 17 0 0 1 3 4c0-.6.4-1 1-1h3.5c.6 0 1 .4 1 1 0 1.3.2 2.5.6 3.6.1.3 0 .7-.2 1z" fill="#1d1d1d"/></svg>
    +353 (0)861 470 295
  </div>

  <svg class="abs banner" viewBox="0 0 805 101" preserveAspectRatio="none">
    <polygon points="287,0 805,0 805,101 193,101" fill="var(--blue)"/>
  </svg>
  <div class="abs banner-title">CORVANE PROJECT SERVICES IS A</div>
  <div class="abs banner-rule"></div>
  <div class="abs banner-sub">leading project control consultancy based in Co. Cork Ireland</div>

  <div class="abs hero" role="img" aria-label="Photo of hands working at a desk with calculators, a notebook, pen and printed charts"></div>

  <div class="abs pill" style="left:0;top:546px;width:149px">About Us</div>
  <div class="abs copy" style="top:580px">
    <p>Our goal is to make successful project delivery more achievable and repeatable.</p>
    <p>We are continually innovating, evolving and learning, utilizing the latest industry tools and techniques to deliver real value to our clients.</p>
    <p>We are passionate about empowering organisations to achieve their objectives, on time and on budget.</p>
  </div>

  <div class="abs pill" style="left:0;top:707px;width:154px">Our Team</div>
  <div class="abs copy" style="top:744px">
    <p>We use highly experienced industry professionals who engage with our clients to deliver practical and innovative project control solutions.</p>
  </div>

  <div class="abs pill" style="left:0;top:811px;width:191px">Our Expertise</div>
  <div class="abs copy" style="top:852px">
    <p>For over 20 years we have been helping our clients to successfully deliver capital projects within the pharmaceutical and biotechnology sectors.</p>
    <p>During this time, we have worked closely with multinational healthcare companies and leading A&amp;E firms, on a variety of business-critical projects.</p>
    <p>Our experience and knowledge of project control gives our client’s unparalleled visibility of Cost, Schedule and Risk through the lifecycle of their projects.</p>
    <p>This visibility allows our clients to make timely informed decisions which increase efficiency and project performance.</p>
  </div>

  <div class="abs pill services" style="left:403px;top:543px;width:184px">Core Services</div>

  <div class="abs timeline"></div>

  <div class="abs svc-icon" style="left:414px;top:623px"><span><svg width="14" height="14" viewBox="0 0 14 14"><rect x="2" y="7" width="2" height="5" fill="#fff"/><rect x="6" y="4" width="2" height="8" fill="#fff"/><rect x="10" y="2" width="2" height="10" fill="#fff"/></svg></span></div>
  <div class="abs svc-title" style="left:467px;top:630px"><b>Planning</b> and Scheduling</div>
  <ul class="abs svc-list" style="left:476px;top:663px">
    <li>Tender Planning</li>
    <li>Interactive Planning / Pull Planning</li>
    <li>CPM Planning &amp; Scheduling</li>
    <li>Agile / Lean Planning Methodology</li>
    <li>Independent Schedule Quality Assessment</li>
    <li>Schedule Risk Analysis (Monte Carlo)</li>
    <li>Training</li>
  </ul>

  <div class="abs svc-icon" style="left:414px;top:786px"><span><svg width="12" height="12" viewBox="0 0 12 12"><rect x="1" y="1" width="10" height="10" rx="2" fill="#fff"/><circle cx="4" cy="4" r="1.2" fill="#2a5db0"/><circle cx="8" cy="8" r="1.2" fill="#2a5db0"/></svg></span></div>
  <div class="abs svc-title" style="left:467px;top:793px"><b>Management</b> of Risk</div>
  <ul class="abs svc-list small" style="left:476px;top:828px">
    <li>Risk Management Policies &amp; Procedures</li>
    <li>Risk Management Strategy</li>
    <li>Risk Registers</li>
    <li>Risk Response and Communication</li>
    <li>Cost &amp; Schedule Risk Analysis (Monte Carlo)</li>
    <li>Risk Management Training</li>
  </ul>

  <div class="abs svc-icon" style="left:414px;top:941px"><span><svg width="12" height="12" viewBox="0 0 12 12"><rect x="2" y="1" width="8" height="10" rx="1" fill="#fff"/><rect x="3.5" y="2.5" width="5" height="2" fill="#2a5db0"/></svg></span></div>
  <div class="abs svc-title" style="left:467px;top:948px"><b>Cost</b> Control</div>
  <ul class="abs svc-list small" style="left:476px;top:983px">
    <li>Estimating &amp; Forecasting</li>
    <li>Earned Value Management</li>
    <li>Progress Reporting</li>
    <li>Cost Risk Analysis (Monte Carlo)</li>
  </ul>

  <div class="abs tools">
    <span>Tallyline</span>
    <span>Keelworks</span>
    <span>Riskora</span>
    <span><i class="sq"></i>Plannex</span>
    <span>Ledgerly</span>
    <span>Cadenta</span>
    <span><i class="sq"></i>Taskfold</span>
  </div>

  <svg class="abs footer" viewBox="0 0 805 96" preserveAspectRatio="none">
    <polygon points="0,44 584,44 650,0 805,0 805,96 0,96" fill="var(--blue)"/>
  </svg>
  <div class="abs portrait" role="img" aria-label="Portrait photo of the managing director"></div>

  <div class="abs contact" style="left:38px">
    <svg width="30" height="20" viewBox="0 0 30 20"><rect x="1" y="1" width="28" height="18" fill="none" stroke="#fff" stroke-width="2"/><polyline points="1,1 15,11 29,1" fill="none" stroke="#fff" stroke-width="2"/></svg>
    info@corvaneservices.ie
  </div>
  <div class="abs divider"></div>
  <div class="abs contact" style="left:396px">
    <svg width="22" height="22" viewBox="0 0 22 22" fill="none" stroke="#fff" stroke-width="1.6"><circle cx="11" cy="11" r="9.5"/><ellipse cx="11" cy="11" rx="4.2" ry="9.5"/><line x1="1.5" y1="11" x2="20.5" y2="11"/><line x1="3" y1="6" x2="19" y2="6"/><line x1="3" y1="16" x2="19" y2="16"/></svg>
    www.corvaneservices.ie
  </div>
  <div class="abs md-name">Derek Halloran</div>
  <div class="abs md-role">(Managing Director)</div>
</div>
</body>
</html>
```